Roofing Company needs YOU to help put us on top!

Brindlecrest Roofing, a fresh new company with quality and Innovation in mind, needs your help to stand out in the competitive Chicago market. With over 30 years of experience, all the right people and tools for the job, the only thing we are missing is your creative ideas in web design to help us grow our online presence.
Our Company offers exceptional quality at reasonable prices, we work for the everyday people both blue collar and white collar.

We have used MakerHarbor in the past with multiple successful campaigns, we are excited to see what you can come up with for our website.

www.BrindlecrestRoofing-demo.net will be the domain

We will be hiring a photographer for visual content on our pages later. Stock photos are okay to use but should follow theme.

Thank you for taking the time on the submissions, if you have any questions don't hesitate to ask and we will provide whatever is needed to you.

Target Market(s)

Homeowners & Commercial Clients between 21-65

Industry/Entity Type

Roofing

Coding

Coded - Design and coding required

Number of Pages Required

4 page

Font styles to use
Sans Serif

Colors
ffffff
ec1f27
000000
5c5c5c
757575
b2b2b2

Requirements
Must have
• Color Scheme - should follow around our logo
• As for pages we were looking for an About, Services, Projects (gallery page) and Contact.
• Main page please include social media links and a a place so people could use coinwell to make payments
• Website should work on desktop as well as mobile platforms
Nice to have
• A Live chat feature would be nice if possible
Should not have
• Obscure Colors or Common web templates

```html
<!DOCTYPE html>
<html lang="en">
<head>
<meta charset="utf-8">
<title>Brindlecrest Roofing</title>
<link href="https://fonts.googleapis.com/css2?family=Open+Sans:wght@400;600;700;800&family=Montserrat:wght@600;700;800&display=swap" rel="stylesheet">
<style>
:root{
  --red:#ec1f27;
  --red-dark:#c4161d;
  --black:#000000;
  --ink:#1e1e1e;
  --dark:#2a2a2a;
  --gray:#5c5c5c;
  --mid:#757575;
  --light:#b2b2b2;
  --pale:#ececec;
  --white:#ffffff;
}
*{box-sizing:border-box;margin:0;padding:0}
html,body{width:1200px;height:2620px;overflow:hidden}
body{font-family:"Open Sans",Arial,sans-serif;color:var(--ink);background:var(--white);position:relative}
.abs{position:absolute}
h1,h2,h3,h4{font-family:"Montserrat","Open Sans",sans-serif}

/* top bar */
.topbar{top:0;left:0;width:1200px;height:32px;background:var(--red);color:var(--white);font-size:11px;display:flex;align-items:center;justify-content:space-between;padding:0 40px}
.topbar span{margin-right:24px}

/* hero */
.hero{top:32px;left:0;width:1200px;height:788px;background:linear-gradient(180deg,#6e8aa6 0%,#a9b6c2 35%,#7b6c60 62%,#3a322d 100%)}
.logo-box{top:32px;left:40px;width:150px;height:70px;background:var(--red);display:flex;align-items:center;justify-content:center;gap:8px;color:var(--white);font-weight:800;font-size:13px;letter-spacing:.5px}
.logo-box i{width:14px;height:14px;background:var(--white);display:block}
.nav{top:44px;left:330px;display:flex;gap:4px}
.nav a{color:var(--white);text-decoration:none;font-size:13px;font-weight:600;padding:10px 20px}
.nav a.active{background:var(--red)}
.phone-box{top:44px;left:970px;width:190px;height:38px;background:rgba(0,0,0,.55);color:var(--white);font-size:14px;font-weight:700;display:flex;align-items:center;justify-content:center;gap:10px}
.hero-tag{top:104px;left:640px;width:470px;text-align:right;color:var(--white)}
.hero-tag p{font-size:22px;font-weight:600;font-style:normal}
.hero-tag h1{font-size:56px;font-weight:800;letter-spacing:1px;line-height:1.05}
.slide-arrow{width:26px;height:40px;background:rgba(0,0,0,.45);display:flex;align-items:center;justify-content:center}
.repair-card{top:372px;left:160px;width:288px;height:448px;background:rgba(20,20,20,.82);color:var(--white);padding:210px 26px 0}
.repair-card h3{font-size:24px;font-weight:600;margin-bottom:10px}
.repair-card p{font-size:11px;line-height:1.6;color:#ddd}
.btn-white{display:inline-block;background:var(--white);color:var(--ink);font-size:11px;font-weight:700;padding:10px 26px;letter-spacing:.5px}
.repair-card .btn-white{position:absolute;left:26px;bottom:26px;width:236px;text-align:center}
.tile{top:580px;width:296px;height:240px}
.tile .label{position:absolute;left:0;bottom:0;width:100%;height:80px;background:linear-gradient(180deg,rgba(0,0,0,0),rgba(0,0,0,.75));color:var(--white);font-family:"Montserrat",sans-serif;font-weight:600;font-size:22px;padding:18px 22px;line-height:1.05}

/* about */
.about{top:820px;left:0;width:1200px;height:400px;background:var(--red);color:var(--white)}
.welcome{top:26px;left:0;width:1200px;text-align:center;font-size:26px;font-weight:600;display:flex;justify-content:center;align-items:center;gap:14px}
.welcome strong{font-weight:800}
.welcome i{width:22px;height:22px;background:var(--white);display:block}
.about-left{top:80px;left:40px;width:540px}
.about-left h2{font-size:18px;font-weight:700;margin-bottom:12px}
.about-left p{font-size:12px;line-height:1.75}
.about-left .btn-white{position:absolute;top:210px;left:0;width:540px;padding:11px 18px}
.about-right{top:80px;left:620px;width:540px}
.about-right .lead{font-size:12px;font-weight:700;line-height:1.6;margin-bottom:14px;text-transform:uppercase}
.ticks{list-style:none}
.ticks li{font-size:11.5px;line-height:1.45;margin-bottom:9px;display:flex;gap:10px;align-items:flex-start}
.ticks svg{flex:none;margin-top:2px}

/* services */
.services{top:1220px;left:0;width:1200px;height:456px;background:linear-gradient(180deg,#f3f3f3,#e2e2e2)}
.section-title{position:absolute;left:0;width:1200px;text-align:center;font-size:26px;font-weight:700}
.section-title::after{content:"";display:block;width:60px;height:3px;background:var(--red);margin:10px auto 0}
.svc{top:118px;width:205px}
.svc .pic{width:205px;height:150px}
.svc h4{font-size:15px;font-weight:700;margin:14px 0 8px}
.svc p{font-size:10.5px;line-height:1.6;color:var(--gray)}
.side-arrow{top:1528px;width:28px;height:42px;background:var(--gray);display:flex;align-items:center;justify-content:center}
.btn-red{display:inline-block;background:var(--red);color:var(--white);font-size:11px;font-weight:700;padding:11px 26px;letter-spacing:.5px}

/* projects */
.projects{top:1676px;left:0;width:1200px;height:400px;background:linear-gradient(160deg,#3d3d3d,#1f1f1f 60%,#2d2926)}
.projects .section-title{color:var(--white);top:54px}
.projects .blurb{position:absolute;top:140px;left:300px;width:600px;text-align:center;color:var(--white);font-size:13px;line-height:1.7}
.projects .blurb em{color:var(--red);font-style:normal;font-weight:700}
.projects .btn-red{position:absolute;top:254px;left:510px;width:180px;text-align:center}

/* red strip */
.strip{top:2076px;left:0;width:1200px;height:26px;background:var(--red);color:var(--white);font-size:10px;display:flex;align-items:center;justify-content:flex-end;gap:22px;padding-right:60px}

/* contact band */
.contact-band{top:2102px;left:0;width:1200px;height:136px;background:var(--mid);color:var(--white);display:flex;justify-content:center;gap:110px;padding-top:40px}
.cinfo{display:flex;gap:14px;width:250px}
.cinfo .ico{width:52px;height:52px;background:var(--white);display:flex;align-items:center;justify-content:center;flex:none}
.cinfo h4{font-size:15px;font-weight:700;color:var(--white);margin-bottom:6px}
.cinfo p{font-size:10.5px;line-height:1.5}

/* footer */
.footer{top:2238px;left:0;width:1200px;height:382px;background:linear-gradient(180deg,#3a3a3a,#242424);color:var(--light)}
.fcol{top:40px}
.fcol h4{font-size:14px;font-weight:600;color:var(--white);margin-bottom:14px}
.fcol ul{list-style:none}
.fcol li{font-size:11px;margin-bottom:8px;display:flex;align-items:center;gap:8px}
.fcol li b{width:10px;height:10px;background:var(--red);display:block}
.field{width:150px;height:22px;background:var(--white);margin-bottom:8px;font-size:9px;color:var(--mid);padding:5px 8px}
.field.tall{height:40px}
.send{width:150px;height:22px;background:var(--red);color:var(--white);font-size:10px;font-weight:700;text-align:center;line-height:22px}
.map{top:50px;left:612px;width:160px;height:140px;background:linear-gradient(135deg,#dfe6d8,#c6d3e0)}
.pay{top:258px;left:60px}
.pay h4{font-size:14px;color:var(--white);font-weight:600;margin-bottom:10px}
.cards{display:flex;gap:6px}
.cards span{width:34px;height:22px;background:var(--white);display:block}
.cards span.wide{width:auto;padding:0 10px;font-size:10px;font-weight:700;color:var(--ink);line-height:22px}
.chat{top:2396px;left:860px;width:160px;height:36px;background:var(--white);border-radius:18px;display:flex;align-items:center;gap:10px;padding:0 6px;font-size:12px;font-weight:700;color:var(--ink)}
.chat .avatar{width:28px;height:28px;border-radius:50%;background:linear-gradient(135deg,#d9b89c,#8d6b55)}
.copy{top:2594px;left:0;width:1200px;height:26px;background:#1a1a1a;color:var(--light);font-size:10px;text-align:center;line-height:26px}
</style>
</head>
<body>

<div class="abs topbar">
  <div><span>Brindlecrest Roofing &amp; Construction Company, Inc.</span><span>info@brindlecrestroofing-demo.net</span></div>
  <div>Call us today: (312) 555-0148</div>
</div>

<section class="abs hero" role="img" aria-label="Roofer in a cap kneeling on a pitched roof, laying new shingles under a clear sky"></section>

<div class="abs logo-box"><i></i>BRINDLECREST ROOFING</div>
<nav class="abs nav">
  <a class="active">Home</a><a>About</a><a>Services</a><a>Projects</a><a>Contact us</a>
</nav>
<div class="abs phone-box">
  <svg width="14" height="14" viewBox="0 0 24 24"><path fill="#fff" d="M6.6 10.8a15 15 0 0 0 6.6 6.6l2.2-2.2a1 1 0 0 1 1-.25 11.4 11.4 0 0 0 3.6.57 1 1 0 0 1 1 1V20a1 1 0 0 1-1 1A17 17 0 0 1 3 4a1 1 0 0 1 1-1h3.5a1 1 0 0 1 1 1c0 1.25.2 2.45.57 3.57a1 1 0 0 1-.25 1z"/></svg>
  (312) 555-0148
</div>

<div class="abs hero-tag">
  <p>Keeping Your Home Safe</p>
  <h1>COMFORTABLE!</h1>
</div>

<div class="abs slide-arrow" style="top:380px;left:0"><svg width="10" height="16" viewBox="0 0 10 16"><path d="M8 2L2 8l6 6" stroke="#fff" stroke-width="2" fill="none"/></svg></div>
<div class="abs slide-arrow" style="top:380px;left:1174px"><svg width="10" height="16" viewBox="0 0 10 16"><path d="M2 2l6 6-6 6" stroke="#fff" stroke-width="2" fill="none"/></svg></div>

<div class="abs repair-card">
  <h3>ROOF REPAIR</h3>
  <p>Leaks, missing shingles and storm wear fixed fast by our crew, with honest quotes and work done right.</p>
  <span class="btn-white">READ MORE</span>
</div>
<div class="abs tile" style="left:448px;background:linear-gradient(160deg,#9a8a7c,#4e4640)" role="img" aria-label="Worker maintaining a shingle roof">
  <div class="label">ROOF<br>MAINTENANCE</div>
</div>
<div class="abs tile" style="left:744px;background:linear-gradient(160deg,#c9cfd4,#6f7478)" role="img" aria-label="Clean metal gutter along a roof edge">
  <div class="label">GUTTER<br>CLEANING</div>
</div>

<section class="abs about">
  <div class="abs welcome">WELCOME TO <i></i><strong>BRINDLECREST ROOFING</strong></div>
  <div class="abs about-left">
    <h2>ABOUT US</h2>
    <p>Our team at Brindlecrest Roofing &amp; Construction Company, Inc. has been a trusted roofing name in the Chicago area, bringing quality and new ideas to every job we take on. <strong>We are a family owned, owner operated company</strong> as well as a <strong>Full Time Professional Roofing Company</strong>. We take pride in caring for every home and business, from a small repair to a full new roof, and we stand behind each project with clear pricing and friendly service.</p>
    <span class="btn-white">READ MORE</span>
  </div>
  <div class="abs about-right">
    <p class="lead">When choosing your contractor please consider the advantages that Brindlecrest Roofing &amp; Construction can offer to you.</p>
    <ul class="ticks">
      <li><svg width="12" height="12" viewBox="0 0 12 12"><path d="M1 6l3 3 7-7" stroke="#fff" stroke-width="2" fill="none"/></svg>We are a locally owned roofing company with over 30 years of combined experience.</li>
      <li><svg width="12" height="12" viewBox="0 0 12 12"><path d="M1 6l3 3 7-7" stroke="#fff" stroke-width="2" fill="none"/></svg>We are fully licensed, bonded and insured for residential work.</li>
      <li><svg width="12" height="12" viewBox="0 0 12 12"><path d="M1 6l3 3 7-7" stroke="#fff" stroke-width="2" fill="none"/></svg>We use only the best quality materials from trusted manufacturers.</li>
      <li><svg width="12" height="12" viewBox="0 0 12 12"><path d="M1 6l3 3 7-7" stroke="#fff" stroke-width="2" fill="none"/></svg>We offer free estimates and inspections on every roof.</li>
      <li><svg width="12" height="12" viewBox="0 0 12 12"><path d="M1 6l3 3 7-7" stroke="#fff" stroke-width="2" fill="none"/></svg>We stand behind all our work with a written workmanship warranty.</li>
      <li><svg width="12" height="12" viewBox="0 0 12 12"><path d="M1 6l3 3 7-7" stroke="#fff" stroke-width="2" fill="none"/></svg>We will leave your site clean and tidy every day until the job is done.</li>
    </ul>
  </div>
</section>

<section class="abs services">
  <h2 class="section-title" style="top:54px">OUR SERVICES</h2>
  <div class="abs svc" style="left:160px"><div class="pic" role="img" aria-label="Shingle roof on a suburban house" style="background:linear-gradient(160deg,#6d6b6a,#3a3634)"></div><h4>SHINGLE ROOFS</h4><p>New shingle roofs and full tear-offs with durable, weather rated materials built for Chicago winters.</p></div>
  <div class="abs svc" style="left:385px"><div class="pic" role="img" aria-label="Flat roof on a commercial building at dusk" style="background:linear-gradient(160deg,#d89a5a,#3b4d6a)"></div><h4>FLAT ROOFS</h4><p>Flat and low slope systems for homes and commercial buildings, sealed tight against leaks.</p></div>
  <div class="abs svc" style="left:610px"><div class="pic" role="img" aria-label="Roofer repairing shingles" style="background:linear-gradient(160deg,#8fa3b8,#5a4a3e)"></div><h4>ROOF REPAIRS</h4><p>Quick, careful repairs for leaks, flashing and damaged shingles to extend the life of your roof.</p></div>
  <div class="abs svc" style="left:835px"><div class="pic" role="img" aria-label="House roof after a storm" style="background:linear-gradient(160deg,#8a8f95,#4a3f38)"></div><h4>STROM DAMAGE</h4><p>Storm and hail damage checks with help through insurance claims from start to finish.</p></div>
  <span class="abs btn-red" style="top:410px;left:525px;width:150px;text-align:center">SEE ALL SERVICES</span>
</section>
<div class="abs side-arrow" style="left:0"><svg width="10" height="16" viewBox="0 0 10 16"><path d="M8 2L2 8l6 6" stroke="#fff" stroke-width="2" fill="none"/></svg></div>
<div class="abs side-arrow" style="left:1172px"><svg width="10" height="16" viewBox="0 0 10 16"><path d="M2 2l6 6-6 6" stroke="#fff" stroke-width="2" fill="none"/></svg></div>

<section class="abs projects" role="img" aria-label="Dark background photo of a finished roofing project">
  <h2 class="section-title">PROJECTS</h2>
  <p class="blurb">Brindlecrest Roofing &amp; Construction Company, Inc. is committed to giving you the best value when you hire our company to do any project on your home. <em>We are available 7 days a week answering your calls.</em> When it comes to your home, think Brindlecrest.</p>
  <span class="btn-red">GET STARTED YOUR PROJECT</span>
</section>

<div class="abs strip"><span>Home</span><span>About</span><span>Services</span><span>Projects</span><span>Contact Us</span></div>

<section class="abs contact-band">
  <div class="cinfo"><div class="ico"><svg width="22" height="22" viewBox="0 0 24 24"><path fill="#757575" d="M12 2a7 7 0 0 0-7 7c0 5 7 13 7 13s7-8 7-13a7 7 0 0 0-7-7zm0 9.5A2.5 2.5 0 1 1 12 6.5a2.5 2.5 0 0 1 0 5z"/></svg></div><div><h4>ADDRESS</h4><p>4120 W Harbor Ave,<br>Chicago, IL 60639</p></div></div>
  <div class="cinfo"><div class="ico"><svg width="22" height="22" viewBox="0 0 24 24"><path fill="#757575" d="M6.6 10.8a15 15 0 0 0 6.6 6.6l2.2-2.2a1 1 0 0 1 1-.25 11.4 11.4 0 0 0 3.6.57 1 1 0 0 1 1 1V20a1 1 0 0 1-1 1A17 17 0 0 1 3 4a1 1 0 0 1 1-1h3.5a1 1 0 0 1 1 1c0 1.25.2 2.45.57 3.57a1 1 0 0 1-.25 1z"/></svg></div><div><h4>PHONE</h4><p>(312) 555-0148<br>(312) 555-0172</p></div></div>
  <div class="cinfo"><div class="ico"><svg width="22" height="22" viewBox="0 0 24 24"><path fill="#757575" d="M3 5h18v14H3zm2 2v.5l7 4.5 7-4.5V7z"/></svg></div><div><h4>E-MAIL</h4><p>info@brindlecrestroofing-demo.net</p></div></div>
</section>

<footer class="abs footer">
  <div class="abs fcol" style="left:200px">
    <h4>Quick Links</h4>
    <ul><li><b></b>Home</li><li><b></b>About</li><li><b></b>Services</li><li><b></b>Projects</li><li><b></b>Contact</li></ul>
  </div>
  <div class="abs fcol" style="left:410px">
    <h4>Contact Us</h4>
    <div class="field">Name</div><div class="field">Email</div><div class="field tall">Message</div><div class="send">SUBMIT</div>
  </div>
  <div class="abs map" role="img" aria-label="Street map of the Chicago office location"></div>
  <div class="abs fcol" style="left:850px">
    <h4>Follow Us</h4>
    <ul><li><b></b>Chatterly</li><li><b></b>Quillpost</li><li><b></b>Circlenet</li><li><b></b>Workweave</li><li><b></b>Clipstream</li></ul>
  </div>
  <div class="abs pay">
    <h4>Payment</h4>
    <div class="cards"><span></span><span></span><span></span><span></span><span class="wide">coinwell</span></div>
  </div>
</footer>

<div class="abs chat"><div class="avatar" role="img" aria-label="Support agent portrait"></div>LIVE CHAT</div>

<div class="abs copy">© 2024 www.BrindlecrestRoofing-demo.net. All rights reserved.</div>

</body>
</html>
```